The Honeycrisp Are Ready: Announcing Apple Picking At Dorn & Wexley

I would like to develop an e-mail notification to send to our subscribers notifying them:
(Announcing to our fans that Honeycrisp Apples are ready for picking)

Header: The Honeycrisp Are Ready!
Now Picking Our Family Favorite Variety
We Wanted To Make Sure You Were The First To Know

Cedar Knoll Is Open 7 Days A Week For Apple Picking

These Will Not Last Long!

Fall Is Back At Dorn & Wexley. This Means Cool, Crisp Fall Days In The Orchard. Warm Cider Donuts & Apple Fritters, Hard Cider Sampling, Pony Rides, Apple Picking & Much More. Come Join Us And Make Fall Memories That Will Last For Generations To Come.

Target Market(s)

Families Looking For Activities In The Fall

Industry/Entity Type

Agri-Tourism

Font styles to use
Other font styles liked:
• DDC Hardware

Colors
0054AA
0677BA
7BADD7
CADEEF
E8F1F8
EB3D1F
EC4F4E
F09395
F8D3D4
FCEDEE

Requirements
Must have
• Call To Action: The Honeycrisp Are Ready!
Nice to have
• Images of the orchard and people picking apples. Please take a look at our website: www.dornandwexley.example for inspiration

```html
<!DOCTYPE html>
<html lang="en">
<head>
<meta charset="utf-8">
<title>The Honeycrisp Are Ready! – Dorn &amp; Wexley</title>
<link rel="stylesheet" href="https://fonts.googleapis.com/css2?family=Montserrat:wght@500;600;700;800&display=swap">
<style>
  :root {
    --orchard-red: #EB3D1F;
    --paper: #FFFFFF;
    --backdrop: #E6E6E6;
    --fleece: #2E3A66;
  }
  * { margin: 0; padding: 0; box-sizing: border-box; }
  html, body { width: 1200px; height: 2161px; overflow: hidden; background: #FFFFFF; }
  body { font-family: "Montserrat", Arial, sans-serif; color: var(--orchard-red); }

  .backdrop {
    position: absolute; left: 40px; top: 49px; width: 1120px; height: 2091px;
    background: var(--backdrop);
  }
  .email {
    position: absolute; left: 138px; top: 138px; width: 923px; height: 1884px;
    background: var(--paper);
    box-shadow: 0 12px 40px rgba(0,0,0,0.22);
    overflow: hidden;
  }
  .email > * { position: absolute; }
  .center { left: 0; width: 923px; text-align: center; }

  .headline {
    top: 80px; font-weight: 800; font-size: 70px; line-height: 75px; letter-spacing: 0.5px;
  }
  .variety-banner {
    left: 160px; top: 292px; width: 604px; height: 145px;
    background: var(--orchard-red); color: var(--paper);
    display: flex; align-items: center; justify-content: center; text-align: center;
    font-weight: 500; font-size: 35px; line-height: 47px; letter-spacing: 1px;
  }
  .first-to-know {
    top: 484px; font-weight: 500; font-size: 34px; line-height: 45px; letter-spacing: 1.5px;
  }
  .first-to-know strong {
    display: block; font-weight: 800; font-size: 68px; line-height: 72px; letter-spacing: 0; margin-top: -2px;
  }
  .open-line { top: 711px; font-weight: 600; font-size: 44px; line-height: 56px; letter-spacing: 0.5px; }
  .picking-line { top: 1039px; font-weight: 600; font-size: 44px; line-height: 56px; letter-spacing: 0.5px; }

  .round-photo { width: 235px; height: 235px; border-radius: 50%; top: 793px; }
  .round-photo--entrance { left: 79px; background: linear-gradient(180deg, #DCEAF5 0%, #A9C98A 55%, #6E9B4C 100%); }
  .round-photo--cider { left: 611px; background: radial-gradient(circle at 45% 40%, #E2503A 0%, #D24A2E 45%, #E9B27A 100%); }
  .days-badge {
    left: 344px; top: 793px; width: 235px; height: 235px; border-radius: 50%;
    background: var(--orchard-red); color: var(--paper);
    display: flex; align-items: center; justify-content: center; text-align: center;
    font-weight: 800; font-size: 50px; line-height: 53px;
  }

  .closing-band {
    left: 0; top: 1378px; width: 923px; height: 506px; background: var(--orchard-red);
  }
  .round-photo--picking {
    left: 243px; top: 1160px; width: 436px; height: 436px; border-radius: 50%;
    background: linear-gradient(170deg, #E4EDF4 0%, #B8C98E 40%, #6F7FA0 75%, var(--fleece) 100%);
  }
  .urgency {
    top: 1616px; color: var(--paper); font-weight: 700; font-size: 49px; line-height: 60px; letter-spacing: 1px;
  }
  .fall-copy {
    top: 1702px; color: var(--paper); white-space: nowrap;
    font-weight: 500; font-size: 22.5px; line-height: 27.3px;
  }
</style>
</head>
<body>
  <div class="backdrop"></div>
  <main class="email">
    <h1 class="headline center">THE HONEYCRISP<br>ARE READY!</h1>

    <div class="variety-banner">NOW PICKING OUR FAMILY<br>FAVORITE VARIETY</div>

    <p class="first-to-know center">WE WANTED TO MAKE SURE<br>YOU WERE THE FIRST<strong>TO KNOW</strong></p>

    <p class="open-line center">Cedar Knoll is Open</p>

    <div class="round-photo round-photo--entrance" role="img" aria-label="Photo of the Dorn &amp; Wexley orchard entrance gate with a path and lawn"></div>
    <div class="days-badge">7 Days<br>a Week</div>
    <div class="round-photo round-photo--cider" role="img" aria-label="Photo of a can of honeycrisp hard cider surrounded by fresh apples and slices"></div>

    <p class="picking-line center">for Apple Picking</p>

    <div class="closing-band"></div>
    <div class="round-photo--picking" role="img" aria-label="Photo of a young child in a fleece jacket reaching up to pick apples from a tree"></div>

    <h2 class="urgency center">THESE WILL NOT LAST LONG!</h2>
    <p class="fall-copy center">Fall Is Back At Dorn &amp; Wexley. This Means Cool, Crisp Fall Days<br>In The Orchard. Warm Cider Donuts &amp; Apple Fritters,<br>Hard Cider Sampling, Pony Rides, Apple Picking<br>&amp; Much More. Come Join Us And Make Fall Memories<br>That Will Last For Generations To Come.</p>
  </main>
</body>
</html>
```